Modern look business card for residential loan officer

I'm looking for a business card design with a very contemporary sexy look. (black with silver embossed print but I am open to ideas??). I am a residential loan officer for higher end clientele and I want a card to promote myself more as the brand and not the company I work for. However, I do need the NMLS numbers with my name and the company name (this is our lending license numbers)

- The front possibly just my name (Dominic R. Patel) and title. Maybe the company logo small in the corner?
- I've attached my email signature for an idea of what I need *omit the fax number
- I like the modern look of the "tide porter" logo that I attached as a guide but again I'm excited to see what examples everyone can come up with.
- Maybe black on black (glossy print)?
- Possibly a contemporary look with my name or "Patel"

Industry/Entity Type

Business

Contact Information for Business Card

Dominic Patel / Loan Officer NMLS: 48106
dpatel@fernwaylending.example
(C) 555-217-4830

Fernway Mortgage NMLS: 204719
(O) 555-403-1962
4 Calloway Ct St. Louis, MO 63000
dpatel.fernwaylending.example

Colors
000000
1b1b1b
333333
5c5c5c
474747

Requirements
Must have
• Modern, sexy, contemporary. Something that will WOW people when they see it!
Nice to have
• Something unique that I can't think of
Should not have
• I don't want a boring white background card like everyone else.
• I'm not affiliated with tide porters. I simply was using that as an example.

```html
<!DOCTYPE html>
<html lang="en">
<head>
<meta charset="utf-8">
<title>Dominic Patel — Loan Officer Business Card</title>
<link rel="stylesheet" href="https://fonts.googleapis.com/css2?family=Great+Vibes&family=Crimson+Text:wght@400;600&display=swap">
<style>
  :root {
    --page-bg: #2a2a2a;
    --card-black: #0d0d0d;
    --damask-dark: #101010;
    --damask-mid: #1f1f1f;
    --gold-deep: #a88a3c;
    --gold: #d9bd6a;
    --gold-light: #f3e3a6;
    --rule: #9a9a9a;
    --ink-light: #f2f2f2;
    --ink-soft: #cfcfcf;
  }
  * { box-sizing: border-box; margin: 0; padding: 0; }
  html, body {
    width: 1200px;
    height: 1023px;
    overflow: hidden;
    background: var(--page-bg);
  }
  .stage {
    width: 1200px;
    height: 1023px;
    display: flex;
    align-items: center;
    justify-content: center;
    gap: 80px;
  }
  .card {
    position: relative;
    width: 390px;
    height: 682px;
    padding: 7px;
    background: linear-gradient(135deg, var(--gold-light), var(--gold-deep) 45%, var(--gold) 70%, var(--gold-deep));
    box-shadow: 0 20px 50px rgba(0,0,0,0.5);
  }
  .card-face {
    position: relative;
    width: 100%;
    height: 100%;
    overflow: hidden;
    background: var(--card-black);
  }
  .damask-field {
    position: absolute;
    inset: 0;
    background: radial-gradient(ellipse at 50% 40%, var(--damask-mid), var(--damask-dark) 75%);
  }
  .skyline-band {
    position: absolute;
    left: 0;
    right: 0;
    height: 150px;
  }
  .skyline-band--bottom {
    bottom: 0;
    background: linear-gradient(180deg, rgba(168,138,60,0) 0%, var(--gold-deep) 30%, var(--gold) 60%, var(--gold-light));
  }
  .skyline-band--top {
    top: 0;
    background: linear-gradient(0deg, rgba(168,138,60,0) 0%, var(--gold-deep) 30%, var(--gold) 60%, var(--gold-light));
  }
  .identity {
    position: absolute;
    top: 80px;
    left: 0;
    right: 0;
    text-align: center;
  }
  .rule {
    display: block;
    width: 270px;
    height: 1px;
    margin: 0 auto;
    background: var(--rule);
  }
  .name {
    font-family: "Great Vibes", cursive;
    font-weight: 400;
    font-size: 60px;
    line-height: 1;
    padding: 22px 0 20px;
    background: linear-gradient(180deg, var(--gold-light), var(--gold) 55%, var(--gold-deep));
    -webkit-background-clip: text;
    background-clip: text;
    color: transparent;
  }
  .title {
    margin-top: 18px;
    font-family: "Crimson Text", serif;
    font-weight: 600;
    font-size: 13px;
    letter-spacing: 1.2px;
    color: var(--ink-light);
  }
  .contact {
    position: absolute;
    top: 320px;
    left: 0;
    right: 0;
    font-family: "Crimson Text", serif;
    font-weight: 600;
    color: var(--ink-light);
  }
  .contact-line {
    display: flex;
    align-items: center;
    justify-content: center;
    gap: 10px;
    margin-bottom: 10px;
  }
  .phone { font-size: 28px; }
  .email { font-size: 20px; }
  .icon { flex: none; }
  .pitch {
    position: absolute;
    top: 210px;
    left: 0;
    right: 0;
    text-align: center;
    font-family: "Crimson Text", serif;
    color: var(--ink-light);
  }
  .pitch-lead {
    font-size: 30px;
    letter-spacing: 4px;
  }
  .pitch-key {
    font-size: 56px;
    font-weight: 600;
    letter-spacing: 6px;
    line-height: 1.1;
    background: linear-gradient(180deg, var(--gold-light), var(--gold) 55%, var(--gold-deep));
    -webkit-background-clip: text;
    background-clip: text;
    color: transparent;
  }
  .company {
    position: absolute;
    bottom: 46px;
    left: 0;
    right: 0;
    text-align: center;
    font-family: "Crimson Text", serif;
    color: var(--ink-soft);
    font-size: 14px;
    line-height: 1.6;
  }
  .company-name {
    font-size: 18px;
    font-weight: 600;
    letter-spacing: 1.5px;
    color: var(--gold);
  }
</style>
</head>
<body>
<main class="stage">
  <article class="card card--front">
    <div class="card-face">
      <div class="damask-field" role="img" aria-label="Black damask floral pattern background"></div>

      <header class="identity">
        <span class="rule"></span>
        <h1 class="name">Dominic Patel</h1>
        <span class="rule"></span>
        <p class="title">LOAN OFFICER &nbsp;|&nbsp; NMLS: 48106</p>
      </header>

      <section class="contact">
        <p class="contact-line phone">
          <svg class="icon" width="16" height="18" viewBox="0 0 20 22" aria-hidden="true">
            <path d="M5 1 L8 6 L6 8 Q8 13 12 16 L14 14 L19 17 L17 21 Q6 19 1 5 Z" fill="var(--gold)"/>
          </svg>
          555-217-4830
        </p>
        <p class="contact-line email">
          <svg class="icon" width="20" height="14" viewBox="0 0 26 18" aria-hidden="true">
            <rect x="1" y="1" width="24" height="16" fill="var(--gold)"/>
            <path d="M1 1 L13 10 L25 1" fill="none" stroke="var(--card-black)" stroke-width="1.8"/>
          </svg>
          dpatel@fernwaylending.example
        </p>
      </section>

      <div class="skyline-band skyline-band--bottom" role="img" aria-label="Gold city skyline silhouette"></div>
    </div>
  </article>

  <article class="card card--back">
    <div class="card-face">
      <div class="damask-field" role="img" aria-label="Black damask floral pattern background"></div>
      <div class="skyline-band skyline-band--top" role="img" aria-label="Gold city skyline silhouette"></div>

      <section class="pitch">
        <p class="pitch-lead">LOOKING FOR</p>
        <p class="pitch-key">DEALS</p>
        <p class="pitch-lead">?</p>
      </section>

      <footer class="company">
        <p class="company-name">Fernway Mortgage</p>
        <p>NMLS: 204719 &nbsp;|&nbsp; (O) 555-403-1962</p>
        <p>4 Calloway Ct St. Louis, MO 63000</p>
        <p>dpatel.fernwaylending.example</p>
      </footer>
    </div>
  </article>
</main>
</body>
</html>
```